I need a two page flyer (one page front and back) outlining our residential furniture rental options.

Title: Premium Residential Furniture Rentals

GOOD
Our Brimwell Orla Furniture Package is designed to offer a perfect balance of affordability and style, without compromising on quality. This package features a selection of functional and aesthetically pleasing furniture pieces, ideal for those looking to create a polished and professional space. With quick installation handled by our experienced in-house team, you can expect a smooth and hassle-free setup. This package ensures both convenience and value, providing a streamlined solution for your needs.
Living room, dining room and bedroom (additional bedrooms available)
- $710/month with a 3 month commitment
- $570/month with a 6 month commitment

BETTER
Our Premium Furniture Package takes comfort and style to the next level, offering an enhanced experience compared to our Orla option. Carefully selected with durability in mind, this package features high-quality, convenient furniture designed for both functionality and aesthetics. Perfect for those seeking a more refined look and superior comfort, it’s ideal for creating a sophisticated and inviting environment. With attention to detail in both design and craftsmanship, the premium package elevates any space, ensuring a higher standard of comfort and style that caters to both employees and clients.
- $1,150/month with a 3 month commitment
- $900/month with a 6 month commitment

BEST
Our Custom Furniture Package offers a tailored experience where you’ll work directly with our expert designer to create the ultimate luxurious and functional space. We include lounging, dining, sleeping and working from home, this package allows you to curate a space that perfectly fits your needs and style. With personalized attention to detail, we ensure every element is designed to provide the highest level of comfort, convenience, and elegance, transforming your space into a sophisticated sanctuary for relaxation and enjoyment.
Please inquire for pricing

www.quilbyhomeleasing.com

```html
<!DOCTYPE html>
<html lang="en">
<head>
<meta charset="utf-8">
<title>Premium Residential Furniture Rentals – Flyer</title>
<link href="https://fonts.googleapis.com/css2?family=Oswald:wght@500;700&family=Source+Sans+3:wght@400;600;700&display=swap" rel="stylesheet">
<style>
  :root {
    --brown: #8d5f3b;
    --brown-dark: #6f4526;
    --ink: #3b3531;
    --navy: #2c2a4a;
    --grey: #9a9a9a;
    --paper: #ffffff;
    --backdrop: #cdc5c1;
  }
  * { box-sizing: border-box; margin: 0; padding: 0; }
  html, body { width: 1200px; height: 447px; overflow: hidden; }
  body {
    background: var(--backdrop);
    font-family: "Source Sans 3", sans-serif;
    color: var(--ink);
    position: relative;
  }
  .page {
    position: absolute;
    top: 12px;
    width: 298px;
    height: 422px;
    background: var(--paper);
    overflow: hidden;
  }
  .page--front { left: 287px; }
  .page--back { left: 615px; }

  .front-backdrop {
    position: absolute; inset: 0;
    background: linear-gradient(160deg, #fbfaf8 0%, #efece8 45%, #f6f4f1 100%);
  }
  .vertical-title {
    position: absolute;
    left: 8px; top: 416px;
    width: 408px; height: 46px;
    transform-origin: 0 0;
    transform: rotate(-90deg);
    display: flex; justify-content: center; align-items: center;
    font-family: "Oswald", sans-serif;
    font-weight: 700;
    font-size: 40px;
    line-height: 46px;
    color: var(--brown);
    white-space: nowrap;
  }
  .vertical-title__text {
    display: inline-block;
    flex-shrink: 0;
    transform: scaleX(0.62);
  }

  .brand { text-align: center; line-height: 1; }
  .brand__name { font-weight: 400; letter-spacing: 0.4px; }
  .brand__rule {
    display: flex; align-items: center; justify-content: center; gap: 5px;
    letter-spacing: 4px;
  }
  .brand__rule::before, .brand__rule::after {
    content: ""; width: 12px; height: 1px; background: currentColor;
  }
  .brand__tag { letter-spacing: 0.5px; }
  .brand__mark {
    display: inline-block; width: 9px; height: 9px;
    border: 1px solid currentColor; margin-right: 4px; vertical-align: -1px;
  }

  .page--front .brand {
    position: absolute; left: 93px; top: 22px; width: 150px; color: var(--navy);
  }
  .page--front .brand__name { font-size: 9px; margin-bottom: 2px; }
  .page--front .brand__rule { font-size: 4.5px; margin-bottom: 3px; }
  .page--front .brand__tag { font-size: 3.6px; }

  .photo { position: absolute; }
  .photo--living {
    left: 93px; top: 66px; width: 150px; height: 209px;
    background: linear-gradient(170deg, #ece9e4 0%, #c9c0b3 40%, #8f8578 70%, #d8d1c6 100%);
  }
  .photo--great-room {
    left: 51px; top: 46px; width: 184px; height: 122px;
    background: linear-gradient(175deg, #cfc8bc 0%, #a89b88 40%, #7d6c58 75%, #b39072 100%);
  }
  .photo--bedroom {
    left: 9px; top: 330px; width: 205px; height: 88px;
    background: linear-gradient(100deg, #d6d6d6 0%, #4b4b4f 35%, #6f6c68 65%, #bdbdbd 100%);
    border-radius: 4px;
  }

  .price { position: absolute; width: 66px; height: 40px; }
  .price svg { position: absolute; inset: 0; }
  .price__text {
    position: absolute; inset: 0;
    display: flex; flex-direction: column; align-items: center; justify-content: center;
    color: var(--brown-dark); text-align: center; line-height: 1;
    transform: rotate(-8deg);
  }
  .price__amount { font-family: "Oswald", sans-serif; font-weight: 500; font-size: 12px; }
  .price__terms { font-size: 4.6px; }

  .tier-title {
    font-family: "Oswald", sans-serif; font-weight: 700;
    line-height: 1; letter-spacing: 0.3px;
  }
  .tier-copy { font-size: 5.1px; line-height: 5.3px; text-align: justify; }
  .rooms { font-weight: 700; font-size: 5.2px; line-height: 6px; text-align: center; }

  .page--front .tier-title { position: absolute; left: 93px; top: 277px; font-size: 16px; color: var(--brown); }
  .page--front .tier-copy { position: absolute; left: 93px; top: 295px; width: 150px; }
  .page--front .rooms { position: absolute; left: 93px; top: 372px; width: 150px; color: var(--brown-dark); }
  .web-bar {
    position: absolute; left: 93px; top: 394px; width: 150px; height: 28px;
    background: var(--brown); color: #fff;
    font-size: 6px; font-weight: 700;
    display: flex; align-items: center; justify-content: center;
  }

  .back-band {
    position: absolute; left: 0; top: 0; width: 100%; height: 247px;
    background: var(--brown);
  }
  .page--back .brand {
    position: absolute; left: 51px; top: 9px; width: 184px; color: #fff; text-align: left;
  }
  .page--back .brand__name { font-size: 11.5px; margin-bottom: 2px; }
  .page--back .brand__rule { font-size: 5px; margin-bottom: 3px; }
  .page--back .brand__tag { font-size: 4.6px; }

  .inquire { position: absolute; left: 193px; top: 148px; width: 54px; height: 34px; }
  .inquire svg { position: absolute; inset: 0; }
  .inquire span {
    position: absolute; inset: 0; display: flex; align-items: center; justify-content: center;
    font-weight: 700; font-size: 5.6px; line-height: 6px; text-align: center; color: var(--ink);
    transform: rotate(-8deg);
  }
  .page--back .tier-title--best { position: absolute; left: 49px; top: 171px; font-size: 16px; color: #fff; }
  .page--back .tier-copy--best { position: absolute; left: 49px; top: 187px; width: 188px; color: #fff; }
  .page--back .tier-title--good { position: absolute; left: 36px; top: 276px; font-size: 16px; color: var(--grey); font-weight: 500; }
  .page--back .tier-copy--good { position: absolute; left: 105px; top: 250px; width: 184px; }
  .page--back .rooms { position: absolute; left: 105px; top: 311px; width: 184px; color: var(--ink); }
</style>
</head>
<body>

<section class="page page--front" aria-label="Flyer front">
  <div class="front-backdrop" role="img" aria-label="Faded photo of a bright furnished living room behind the page"></div>
  <h1 class="vertical-title"><span class="vertical-title__text">Premium&nbsp; Residential&nbsp; Furniture&nbsp; Rentals</span></h1>

  <div class="brand">
    <div class="brand__name"><span class="brand__mark"></span>QUILBY HOME</div>
    <div class="brand__rule">LEASING</div>
    <div class="brand__tag">STAGING | RESIDENTIAL | CORPORATE | SALES</div>
  </div>

  <div class="photo photo--living" role="img" aria-label="Photo of a staged living room with cream sofas, round coffee tables, patterned rug and large abstract wall art"></div>

  <div class="price" style="left:188px; top:187px;">
    <svg viewBox="0 0 66 40"><ellipse cx="33" cy="20" rx="31" ry="17.5" fill="#fff" stroke="#8d5f3b" stroke-width="2.5" transform="rotate(-8 33 20)"/></svg>
    <div class="price__text"><span class="price__amount">$1,150/</span><span class="price__terms">month with a<br>3 month commitment</span></div>
  </div>
  <div class="price" style="left:188px; top:234px;">
    <svg viewBox="0 0 66 40"><ellipse cx="33" cy="20" rx="31" ry="17.5" fill="#fff" stroke="#8d5f3b" stroke-width="2.5" transform="rotate(-8 33 20)"/></svg>
    <div class="price__text"><span class="price__amount">$900/</span><span class="price__terms">month with a<br>6 month commitment</span></div>
  </div>

  <h2 class="tier-title">BETTER</h2>
  <p class="tier-copy">Our Premium Furniture Package takes comfort and style to the next level, offering an enhanced experience compared to our Orla option. Carefully selected with durability in mind, this package features high-quality, convenient furniture designed for both functionality and aesthetics. Perfect for those seeking a more refined look and superior comfort, it’s ideal for creating a sophisticated and inviting environment. With attention to detail in both design and craftsmanship, the premium package elevates any space, ensuring a higher standard of comfort and style that caters to both employees and clients.</p>
  <p class="rooms">Living room, Dining room and Bedroom<br>(additional bedrooms available)</p>
  <div class="web-bar">www.quilbyhomeleasing.com</div>
</section>

<section class="page page--back" aria-label="Flyer back">
  <div class="back-band"></div>
  <div class="brand">
    <div class="brand__name"><span class="brand__mark"></span>QUILBY HOME</div>
    <div class="brand__rule">LEASING</div>
    <div class="brand__tag">STAGING | RESIDENTIAL | CORPORATE | SALES</div>
  </div>

  <div class="photo photo--great-room" role="img" aria-label="Photo of a large great room with grey sectional sofa, lit built-in shelves, fireplace and chandelier"></div>

  <div class="inquire">
    <svg viewBox="0 0 54 34"><ellipse cx="27" cy="17" rx="25" ry="14.5" fill="#fff" stroke="#6f4526" stroke-width="1.5" transform="rotate(-8 27 17)"/></svg>
    <span>Please inquire<br>for pricing</span>
  </div>

  <h2 class="tier-title tier-title--best">BEST</h2>
  <p class="tier-copy tier-copy--best">Our Custom Furniture Package offers a tailored experience where you’ll work directly with our expert designer to create the ultimate luxurious and functional space. We include lounging, dining, sleeping and working from home, this package allows you to curate a space that perfectly fits your needs and style. With personalized attention to detail, we ensure every element is designed to provide the highest level of comfort, convenience, and elegance, transforming your space into a sophisticated sanctuary for relaxation and enjoyment.</p>

  <h2 class="tier-title tier-title--good">GOOD</h2>
  <p class="tier-copy tier-copy--good">Our Brimwell Orla Furniture Package is designed to offer a perfect balance of affordability and style, without compromising on quality. This package features a selection of functional and aesthetically pleasing furniture pieces, ideal for those looking to create a polished and professional space. With quick installation handled by our experienced in-house team, you can expect a smooth and hassle-free setup. This package ensures both convenience and value, providing a streamlined solution for your needs.</p>
  <p class="rooms">Living room, dining room and bedroom<br>(additional bedrooms available)</p>

  <div class="photo photo--bedroom" role="img" aria-label="Product photo of a bedroom set: tufted grey upholstered bed, grey wood dresser, nightstand and white table lamp"></div>

  <div class="price" style="left:226px; top:328px;">
    <svg viewBox="0 0 66 40"><ellipse cx="33" cy="20" rx="31" ry="17.5" fill="#fff" stroke="#8d5f3b" stroke-width="2.5" transform="rotate(-8 33 20)"/></svg>
    <div class="price__text"><span class="price__amount">$710/</span><span class="price__terms">month with a<br>3 month commitment</span></div>
  </div>
  <div class="price" style="left:226px; top:372px;">
    <svg viewBox="0 0 66 40"><ellipse cx="33" cy="20" rx="31" ry="17.5" fill="#fff" stroke="#8d5f3b" stroke-width="2.5" transform="rotate(-8 33 20)"/></svg>
    <div class="price__text"><span class="price__amount">$570/</span><span class="price__terms">month with a<br>6 month commitment</span></div>
  </div>
</section>

</body>
</html>
```